Buch-/eBook-Cover für Naturheilverfahren
Zielgruppe
Der Rothfeld Verlag ist auf Sachbücher spezialisiert.
Aufgabenstellung
Bitte dazu das beigefügte ausführliche Briefing lesen.

```html
<!DOCTYPE html>
<html lang="de">
<head>
<meta charset="utf-8">
<title>Multitalent Hallbergkur – Buchcover</title>
<link rel="stylesheet" href="https://fonts.googleapis.com/css2?family=Bebas+Neue&family=Roboto:wght@400&display=swap">
<style>
  :root {
    --cream: #fef1de;
    --spine: #fde2b3;
    --orange: #f7a800;
    --orange-text: #f5a600;
    --light-cream: #fde6c4;
    --white: #ffffff;
    --navy: #0b4a82;
    --badge-blue: #a9bbe3;
  }
  * { margin: 0; padding: 0; box-sizing: border-box; }
  html, body { width: 1200px; height: 819px; overflow: hidden; background: var(--white); }
  .cover { position: relative; width: 1200px; height: 819px; overflow: hidden; background: var(--white); }

  .back { position: absolute; left: 0; top: 0; width: 572px; height: 819px; background: var(--cream); }
  .back-title {
    position: absolute; left: 55px; top: 124px;
    font: 47px/1 "Bebas Neue", sans-serif; color: var(--orange-text); letter-spacing: 0.5px;
  }
  .back-text {
    position: absolute; left: 55px; top: 182px; width: 475px;
    font: 15.6px/22.7px "Roboto", sans-serif; color: var(--orange-text);
  }
  .back-text p + p { margin-top: 22.7px; }
  .back-portrait { position: absolute; left: 55px; top: 516px; }
  .back-author { position: absolute; left: 207px; top: 552px; color: var(--orange-text); font-family: "Bebas Neue", sans-serif; }
  .back-author .degree { display: block; font-size: 23px; line-height: 1; }
  .back-author .name { display: block; font-size: 35px; line-height: 1; letter-spacing: 1px; margin-top: 1px; }

  .spine { position: absolute; left: 572px; top: 0; width: 56px; height: 819px; background: var(--spine); }
  .spine-text {
    position: absolute; left: 50%; transform-origin: center; white-space: nowrap;
    font: 33px/1 "Bebas Neue", sans-serif; color: var(--orange-text); letter-spacing: 1px;
  }
  .spine-title { top: 291px; transform: translate(-50%, -50%) rotate(-90deg); }
  .spine-author { top: 602px; transform: translate(-50%, -50%) rotate(-90deg); }

  .front { position: absolute; left: 628px; top: 0; width: 572px; height: 819px; background: var(--white); }
  .photo { position: absolute; }
  .photo-fruit { left: 0; top: 0; width: 212px; height: 224px; background: linear-gradient(135deg, #e6ecea 0%, #e85a50 45%, #3c5a32 75%, #d83a46 100%); }
  .photo-hike { left: 219px; top: 0; width: 353px; height: 224px; background: linear-gradient(180deg, #7f98a0 0%, #5f8a4a 45%, #4d7a2e 100%); }
  .photo-relax { left: 0; top: 478px; width: 572px; height: 341px; background: linear-gradient(160deg, #9b8a78 0%, #c9b8a4 40%, #8cb43a 75%, #6e5a44 100%); }

  .band { position: absolute; left: 0; top: 231px; width: 572px; height: 242px; background: var(--orange); }
  .front-author { position: absolute; left: 149px; top: 242px; color: var(--white); font-family: "Bebas Neue", sans-serif; white-space: nowrap; }
  .front-author .degree { font-size: 24px; }
  .front-author .name { font-size: 34px; letter-spacing: 1.5px; margin-left: 4px; }
  .title-line1 { position: absolute; left: 34px; top: 272px; font: 98px/1 "Bebas Neue", sans-serif; color: var(--white); letter-spacing: 1px; }
  .title-line2 { position: absolute; left: 148px; top: 351px; font: 94px/1 "Bebas Neue", sans-serif; color: var(--light-cream); letter-spacing: 1px; }
  .subtitle { position: absolute; left: 34px; top: 433px; font: 29px/1 "Bebas Neue", sans-serif; color: var(--light-cream); white-space: nowrap; }

  .front-portrait { position: absolute; left: 417px; top: 186px; }

  .badge { position: absolute; left: 361px; top: 526px; width: 172px; height: 172px; }
  .badge-text {
    position: absolute; left: 0; top: 0; width: 172px; height: 172px;
    display: flex; flex-direction: column; justify-content: center; align-items: center;
    transform: rotate(-5deg); text-align: center;
    font: 25px/0.95 "Bebas Neue", sans-serif; color: var(--badge-blue);
  }
  .badge-text .strong { color: var(--white); }
</style>
</head>
<body>
<div class="cover">

  <section class="back">
    <h2 class="back-title">Multitalent Hallbergkur</h2>
    <div class="back-text">
      <p>Lorem ipsum dolor sit amet, consectetuer adipiscing elit. Aenean commodo ligula eget dolor. Aenean massa. Cum sociis natoque penatibus et magnis dis parturient montes, nascetur ridiculus mus. Donec quam felis, ultricies nec, pellentesque eu, pretium quis, sem. Nulla consequat massa quis enim.</p>
      <p>Donec pede justo, fringilla vel, aliquet nec, vulputate eget, arcu. In enim justo, rhoncus ut, imperdiet a, venenatis vitae, justo. Nullam dictum felis eu pede mollis pretium. Integer tincidunt. Cras dapibus. Vivamus elementum semper nisi. Aenean vulputate eleifend tellus.</p>
      <p>Aenean leo ligula, porttitor eu, consequat vitae, eleifend ac, enim. Aliquam lorem ante, dapibus in, viverra quis, feugiat a, tellus.</p>
    </div>
    <svg class="back-portrait" width="136" height="136" viewBox="0 0 136 136" role="img" aria-label="Porträtfoto der Autorin">
      <defs><radialGradient id="portraitBack" cx="50%" cy="50%" r="50%"><stop offset="0%" stop-color="#d9a88c"/><stop offset="100%" stop-color="#6a4a34"/></radialGradient></defs>
      <circle cx="68" cy="68" r="66" fill="url(#portraitBack)" stroke="#ffffff" stroke-width="4"/>
    </svg>
    <div class="back-author"><span class="degree">Dr. med.</span><span class="name">Carola Wenzel</span></div>
  </section>

  <section class="spine">
    <div class="spine-text spine-title">Multitalent Hallbergkur</div>
    <div class="spine-text spine-author">Dr. med. Carola Wenzel</div>
  </section>

  <section class="front">
    <div class="photo photo-fruit" role="img" aria-label="Foto: Wassermelone in Herzform mit Heidelbeeren, Brombeeren und Minze"></div>
    <div class="photo photo-hike" role="img" aria-label="Foto: Paar macht Rast auf einer Bergwiese mit Talblick"></div>

    <div class="band"></div>
    <div class="front-author"><span class="degree">Dr. med.</span><span class="name">Carola Wenzel</span></div>
    <h1>
      <span class="title-line1">Multitalent</span>
      <span class="title-line2">Hallbergkur</span>
    </h1>
    <p class="subtitle">Regeneration, Fasten und Detox nach Johann Hallberg</p>

    <svg class="front-portrait" width="138" height="138" viewBox="0 0 138 138" role="img" aria-label="Porträtfoto der Autorin">
      <defs><radialGradient id="portraitFront" cx="50%" cy="50%" r="50%"><stop offset="0%" stop-color="#d9a88c"/><stop offset="100%" stop-color="#5e6a48"/></radialGradient></defs>
      <circle cx="69" cy="69" r="66" fill="url(#portraitFront)" stroke="#ffffff" stroke-width="4"/>
    </svg>

    <div class="photo photo-relax" role="img" aria-label="Foto: Zwei Personen in Bademänteln entspannen im Ruheraum mit Holzwänden"></div>

    <div class="badge">
      <svg width="172" height="172" viewBox="0 0 172 172" aria-hidden="true">
        <circle cx="86" cy="86" r="83" fill="var(--navy)" stroke="#ffffff" stroke-width="4"/>
      </svg>
      <div class="badge-text">
        <span>Mit</span>
        <span class="strong">Low-Carb-</span>
        <span><span class="strong">Rezepten</span> für</span>
        <span>einen gesunden</span>
        <span>Lebensstil</span>
      </div>
    </div>
  </section>

</div>
</body>
</html>
```